IT Company based on Biology Business Needs a PowerPoint Design

We need a powerpoint design for a new company called 'Tall FERN'. We develop the machine learning solutions especially focused on deep learning algorithms for biology industry. Our initial product is a vision detection on biological images to help doctors diagnose the symptoms. We would like to see designs that use the color green.

Industry/Entity Type

Biotechnology

Requirements
Nice to have
• Lots of slide templates with company logo's look and feel

```html
<!DOCTYPE html>
<html lang="en">
<head>
<meta charset="utf-8">
<title>Tall FERN – Slide Templates</title>
<link href="https://fonts.googleapis.com/css2?family=Abel&family=Open+Sans:wght@400;700&family=Roboto+Condensed:wght@400;700&display=swap" rel="stylesheet">
<style>
:root{
  --green:#138c45;
  --lime:#7cc242;
  --ink:#444;
  --muted:#5a5a5a;
  --strip:#d2d2d2;
  --panel:#f1f2f4;
  --board:#000;
  --white:#fff;
}
*{box-sizing:border-box;margin:0;padding:0}
html,body{width:1033px;height:1200px;overflow:hidden;background:var(--board)}
.board{position:relative;width:1080px;height:1254px;transform:scale(.9565,.957);transform-origin:0 0}
.slide{position:absolute;width:513px;height:385px;background:var(--white);overflow:hidden;font-family:"Open Sans",Arial,sans-serif;color:var(--ink)}
.s1{left:18px;top:24px}.s2{left:548px;top:24px}
.s3{left:18px;top:434px}.s4{left:548px;top:434px}
.s5{left:18px;top:842px}.s6{left:548px;top:840px;background:var(--green)}
.footer{position:absolute;left:0;right:0;bottom:0;height:9px;background:var(--strip)}
.header{position:absolute;left:0;top:0;right:0;height:37px;background:var(--green);border-bottom:2px solid var(--white);box-shadow:0 2px 0 var(--lime)}
.header h2{position:absolute;left:12px;top:7px;font:400 17px "Abel",sans-serif;color:var(--white);letter-spacing:.3px}
.brand{font-family:"Open Sans",Arial,sans-serif;font-weight:700;letter-spacing:-.5px;display:flex;align-items:center;gap:4px;white-space:nowrap}
.brand .dot{border-radius:50%;flex:none}
.header .brand{position:absolute;right:8px;top:12px;font-size:11px;color:var(--white)}
.header .brand .dot{width:8px;height:8px;background:var(--white)}
/* cover */
.cover-band{position:absolute;left:0;top:0;right:0;height:242px;background:var(--green);border-bottom:3px solid var(--lime)}
.cover-band h1{position:absolute;top:96px;width:100%;text-align:center;font:400 25px "Abel",sans-serif;color:var(--white)}
.cover-band p{position:absolute;top:130px;width:100%;text-align:center;font:400 14px "Abel",sans-serif;color:var(--white)}
.s1 .brand{position:absolute;left:168px;top:292px;font-size:32px;color:var(--lime)}
.s1 .brand .dot{width:16px;height:16px;background:var(--green)}
/* content */
.item{position:absolute;left:22px;width:470px}
.item h3,.lead h3{font-size:9px;font-weight:700;color:var(--lime);display:flex;align-items:center;gap:8px;margin-bottom:3px}
.item h3::before,.lead h3::before{content:"";width:9px;height:9px;border-radius:50%;background:var(--green)}
.item p{margin-left:21px;font-size:7.2px;line-height:12.8px;color:var(--ink)}
.col{position:absolute;left:22px;width:260px;font-size:7.2px;line-height:12.8px}
.col p{margin-left:21px;width:234px}
.photo{position:absolute;left:303px;top:67px;width:210px;height:289px;background:linear-gradient(160deg,#8fa3b8 0%,#3b4a60 35%,#12161e 65%,#c9ccd0 100%)}
.placeholder{position:absolute;left:308px;width:181px;height:119px;background:#ececec}
/* timeline */
.lead{position:absolute;left:23px;top:55px;width:470px}
.lead h3::before{display:none}
.lead p{font-size:7.2px;line-height:12.8px;margin-top:10px}
.rail{position:absolute;left:95px;top:152px;width:325px;height:2px;background:#d8d8d8}
.year{position:absolute;top:130px;width:44px;height:44px;border-radius:50%;border:3px solid #e6e6e6;color:var(--white);font:700 12px "Open Sans",sans-serif;display:flex;align-items:center;justify-content:center}
.card{position:absolute;top:178px;width:142px;height:170px;background:var(--panel);border:1px solid var(--c);border-radius:2px}
.card h4{height:26px;background:var(--c);color:var(--white);font:700 10px "Roboto Condensed",sans-serif;text-align:center;line-height:28px;position:relative}
.card h4::before{content:"";position:absolute;left:50%;top:-6px;margin-left:-6px;border:6px solid transparent;border-top:0;border-bottom-color:var(--c)}
.card p{font-size:7.2px;line-height:12.8px;padding:10px 14px 0 15px;color:var(--ink)}
.c1{left:25px;--c:var(--green)}.c2{left:186px;--c:var(--lime)}.c3{left:349px;--c:var(--muted)}
.y1{left:73px;background:var(--green)}.y2{left:234px;background:var(--lime)}.y3{left:398px;background:var(--muted)}
/* closing */
.s6 h2{position:absolute;left:275px;top:106px;font:400 22px "Roboto Condensed",sans-serif;color:var(--white)}
.contact{position:absolute;left:274px;top:153px;width:239px;height:140px;background:var(--white);padding:11px 14px;font-size:12px;line-height:16.5px;color:var(--ink)}
.contact ul{list-style:none;margin-top:14px}
.contact li{display:flex;align-items:center;gap:8px;font-size:12px;line-height:16px}
.contact svg{width:10px;height:10px;flex:none}
.s6 .brand{position:absolute;left:52px;top:202px;font-size:32px;color:var(--white)}
.s6 .brand .dot{width:16px;height:16px;background:var(--white)}
</style>
</head>
<body>
<main class="board">

  <section class="slide s1">
    <div class="cover-band">
      <h1>Project Title Here</h1>
      <p>Subtext here</p>
    </div>
    <div class="brand"><span class="dot"></span>TALL FERN</div>
    <div class="footer"></div>
  </section>

  <section class="slide s2">
    <header class="header"><h2>Project Title Here</h2><div class="brand"><span class="dot"></span>TALL FERN</div></header>
    <div class="item" style="top:64px"><h3>Lorem ipsum dolor sit Lorem ipsum dolor sit &nbsp;Lorem ipsum dolor sit</h3><p>Lorem ipsum dolor sit Lorem ipsum dolor sit &nbsp;Lorem ipsum dolor sit Lorem ipsum dolor sit &nbsp;Lorem ipsum dolor sit Lorem ipsum dolor sit &nbsp;Lorem ipsum dolor sit Lorem ipsum dolor sit &nbsp;Lorem ipsum dolor sit Lorem ipsum dolor sit &nbsp;Lorem ipsum dolor sit Lorem ipsum dolor sit Lorem ipsum dolor sit &nbsp;Lorem ipsum dolor sit Lorem ipsum dolor sit &nbsp;Lorem ipsum dolor sit Lorem ipsum dolor sit</p></div>
    <div class="item" style="top:142px"><h3>Lorem ipsum dolor sit Lorem ipsum dolor sit &nbsp;Lorem ipsum dolor sit</h3><p>Lorem ipsum dolor sit Lorem ipsum dolor sit &nbsp;Lorem ipsum dolor sit Lorem ipsum dolor sit &nbsp;Lorem ipsum dolor sit Lorem ipsum dolor sit &nbsp;Lorem ipsum dolor sit Lorem ipsum dolor sit &nbsp;Lorem ipsum dolor sit Lorem ipsum dolor sit &nbsp;Lorem ipsum dolor sit Lorem ipsum dolor sit Lorem ipsum dolor sit &nbsp;Lorem ipsum dolor sit Lorem ipsum dolor sit &nbsp;Lorem ipsum dolor sit Lorem ipsum dolor sit</p></div>
    <div class="item" style="top:219px"><h3>Lorem ipsum dolor sit Lorem ipsum dolor sit &nbsp;Lorem ipsum dolor sit</h3><p>Lorem ipsum dolor sit Lorem ipsum dolor sit &nbsp;Lorem ipsum dolor sit Lorem ipsum dolor sit &nbsp;Lorem ipsum dolor sit Lorem ipsum dolor sit &nbsp;Lorem ipsum dolor sit Lorem ipsum dolor sit &nbsp;Lorem ipsum dolor sit Lorem ipsum dolor sit &nbsp;Lorem ipsum dolor sit Lorem ipsum dolor sit Lorem ipsum dolor sit &nbsp;Lorem ipsum dolor sit Lorem ipsum dolor sit &nbsp;Lorem ipsum dolor sit Lorem ipsum dolor sit</p></div>
    <div class="item" style="top:297px"><h3>Lorem ipsum dolor sit Lorem ipsum dolor sit &nbsp;Lorem ipsum dolor sit</h3><p>Lorem ipsum dolor sit Lorem ipsum dolor sit &nbsp;Lorem ipsum dolor sit Lorem ipsum dolor sit &nbsp;Lorem ipsum dolor sit Lorem ipsum dolor sit &nbsp;Lorem ipsum dolor sit Lorem ipsum dolor sit &nbsp;Lorem ipsum dolor sit Lorem ipsum dolor sit &nbsp;Lorem ipsum dolor sit Lorem ipsum dolor sit Lorem ipsum dolor sit &nbsp;Lorem ipsum dolor sit Lorem ipsum dolor sit &nbsp;Lorem ipsum dolor sit Lorem ipsum dolor sit</p></div>
    <div class="footer"></div>
  </section>

  <section class="slide s3">
    <header class="header"><h2>Project Title Here</h2><div class="brand"><span class="dot"></span>TALL FERN</div></header>
    <div class="col" style="top:67px"><div class="item" style="position:static;width:auto"><h3>Lorem ipsum dolor sit Lorem ipsum dolor sit</h3></div>
      <p>Lorem ipsum dolor sit Lorem ipsum dolor sit &nbsp;Lorem ipsum dolor sit Lorem ipsum dolor sit Lorem ipsum dolor sit &nbsp;Lorem ipsum dolor sit Lorem ipsum dolor sit Lorem ipsum dolor sit &nbsp;Lorem ipsum dolor sit Lorem ipsum dolor sit Lorem ipsum dolor sit &nbsp;Lorem ipsum dolor sit Lorem ipsum dolor sit Lorem ipsum dolor sit &nbsp;Lorem ipsum dolor sit Lorem ipsum dolor sit</p></div>
    <div class="col" style="top:177px"><p>Lorem ipsum dolor sit Lorem ipsum dolor sit &nbsp;Lorem ipsum dolor sit Lorem ipsum dolor sit Lorem ipsum dolor sit &nbsp;Lorem ipsum dolor sit Lorem ipsum dolor sit Lorem ipsum dolor sit &nbsp;Lorem ipsum dolor sit Lorem ipsum dolor sit Lorem ipsum dolor sit &nbsp;Lorem ipsum dolor sit Lorem ipsum dolor sit Lorem ipsum dolor sit &nbsp;Lorem ipsum dolor sit Lorem ipsum dolor sit</p></div>
    <div class="col" style="top:289px"><p>Lorem ipsum dolor sit Lorem ipsum dolor sit &nbsp;Lorem ipsum dolor sit Lorem ipsum dolor sit Lorem ipsum dolor sit &nbsp;Lorem ipsum dolor sit Lorem ipsum dolor sit Lorem ipsum dolor sit &nbsp;Lorem ipsum dolor sit Lorem ipsum dolor sit Lorem ipsum dolor sit &nbsp;Lorem ipsum dolor sit Lorem ipsum dolor sit Lorem ipsum dolor sit &nbsp;Lorem ipsum dolor sit Lorem ipsum dolor sit</p></div>
    <div class="photo" role="img" aria-label="Photo of a data centre aisle with server racks"></div>
    <div class="footer"></div>
  </section>

  <section class="slide s4">
    <header class="header"><h2>Project Title Here</h2><div class="brand"><span class="dot"></span>TALL FERN</div></header>
    <div class="lead"><h3>Lorem ipsum dolor sit Lorem ipsum dolor sit &nbsp;Lorem ipsum dolor sit</h3>
      <p>Lorem ipsum dolor sit Lorem ipsum dolor sit &nbsp;Lorem ipsum dolor sit Lorem ipsum dolor sit &nbsp;Lorem ipsum dolor sit Lorem ipsum dolor sit &nbsp;Lorem ipsum dolor sit Lorem ipsum dolor sit &nbsp;Lorem ipsum dolor sit Lorem ipsum dolor sit &nbsp;Lorem ipsum dolor sit Lorem ipsum dolor sit Lorem ipsum dolor sit &nbsp;Lorem ipsum dolor sit Lorem ipsum dolor sit &nbsp;Lorem ipsum dolor sit Lorem ipsum dolor sit</p></div>
    <div class="rail"></div>
    <div class="year y1">1995</div><div class="year y2">2005</div><div class="year y3">2015</div>
    <div class="card c1"><h4>TITLE HERE</h4><p>Lorem ipsum dolor sit Lorem ipsum dolor sit &nbsp;Lorem ipsum dolor sit Lorem ipsum dolor sit Lorem ipsum dolor sit Lorem ipsum dolor sit Lorem ipsum dolor sit Lorem ipsum dolor sit Lorem ipsum dolor sit &nbsp;Lorem ipsum dolor sit</p></div>
    <div class="card c2"><h4>TITLE HERE</h4><p>Lorem ipsum dolor sit Lorem ipsum dolor sit &nbsp;Lorem ipsum dolor sit Lorem ipsum dolor sit Lorem ipsum dolor sit Lorem ipsum dolor sit Lorem ipsum dolor sit Lorem ipsum dolor sit Lorem ipsum dolor sit &nbsp;Lorem ipsum dolor sit</p></div>
    <div class="card c3"><h4>TITLE HERE</h4><p>Lorem ipsum dolor sit Lorem ipsum dolor sit &nbsp;Lorem ipsum dolor sit Lorem ipsum dolor sit Lorem ipsum dolor sit Lorem ipsum dolor sit Lorem ipsum dolor sit Lorem ipsum dolor sit Lorem ipsum dolor sit &nbsp;Lorem ipsum dolor sit</p></div>
    <div class="footer"></div>
  </section>

  <section class="slide s5">
    <header class="header"><h2>Project Title Here</h2><div class="brand"><span class="dot"></span>TALL FERN</div></header>
    <div class="col" style="top:67px"><div class="item" style="position:static;width:auto"><h3>Lorem ipsum dolor sit Lorem ipsum dolor sit</h3></div>
      <p>Lorem ipsum dolor sit Lorem ipsum dolor sit &nbsp;Lorem ipsum dolor sit Lorem ipsum dolor sit Lorem ipsum dolor sit &nbsp;Lorem ipsum dolor sit Lorem ipsum dolor sit Lorem ipsum dolor sit &nbsp;Lorem ipsum dolor sit Lorem ipsum dolor sit Lorem ipsum dolor sit &nbsp;Lorem ipsum dolor sit Lorem ipsum dolor sit Lorem ipsum dolor sit &nbsp;Lorem ipsum dolor sit Lorem ipsum dolor sit</p></div>
    <div class="col" style="top:177px"><p>Lorem ipsum dolor sit Lorem ipsum dolor sit &nbsp;Lorem ipsum dolor sit Lorem ipsum dolor sit Lorem ipsum dolor sit &nbsp;Lorem ipsum dolor sit Lorem ipsum dolor sit Lorem ipsum dolor sit &nbsp;Lorem ipsum dolor sit Lorem ipsum dolor sit Lorem ipsum dolor sit &nbsp;Lorem ipsum dolor sit Lorem ipsum dolor sit Lorem ipsum dolor sit &nbsp;Lorem ipsum dolor sit Lorem ipsum dolor sit</p></div>
    <div class="col" style="top:289px"><p>Lorem ipsum dolor sit Lorem ipsum dolor sit &nbsp;Lorem ipsum dolor sit Lorem ipsum dolor sit Lorem ipsum dolor sit &nbsp;Lorem ipsum dolor sit Lorem ipsum dolor sit Lorem ipsum dolor sit &nbsp;Lorem ipsum dolor sit Lorem ipsum dolor sit Lorem ipsum dolor sit &nbsp;Lorem ipsum dolor sit Lorem ipsum dolor sit Lorem ipsum dolor sit &nbsp;Lorem ipsum dolor sit Lorem ipsum dolor sit</p></div>
    <div class="placeholder" style="top:80px"></div>
    <div class="placeholder" style="top:228px"></div>
    <div class="footer"></div>
  </section>

  <section class="slide s6">
    <div class="brand"><span class="dot"></span>TALL FERN</div>
    <h2>Thanks for your Time</h2>
    <div class="contact">
      <p>Lorem ipsum dolor sit amet,<br>consectetur adipiscing elit.<br>Donec accumsan.</p>
      <ul>
        <li><svg viewBox="0 0 10 10"><path d="M2 0.5 L4 0.5 L4.5 3 L3.3 3.8 Q4.2 5.8 6.2 6.7 L7 5.5 L9.5 6 L9.5 8 Q9 9.5 7.5 9.5 Q0.5 8.5 0.5 2.5 Q0.5 1 2 0.5Z" fill="#444"/></svg>: &nbsp;555 0147 2280</li>
        <li><svg viewBox="0 0 10 10"><rect x="0.5" y="2" width="9" height="6.5" fill="#444"/><path d="M0.5 2 L5 5.8 L9.5 2" stroke="#fff" stroke-width="0.9" fill="none"/></svg>: &nbsp;hello@tallfern.com</li>
        <li><svg viewBox="0 0 10 10"><path d="M9.5 0.5 L0.5 4.5 L4.5 5.5 L5.5 9.5Z" fill="#444"/></svg>: &nbsp;tallfern.com</li>
      </ul>
    </div>
  </section>

</main>
</body>
</html>
```